pet resort day care for our buisiness

we need a new web design for our pet center in Florida , we are provide the following services -
1. dog day car
2.dog/cat boarding
3. dog grooming
4. Dog training
5.pet food toy and clothing
our current websit is -http://www.tallowfieldanimalhaven.example/
we are looking for a fresh new design that will reflect the change that we have made in the vusness from renovationnto the facelaty new management and new servises
Target Market(s)
Dog Lover , Upmarket
Industry/Entity Type
Pet
Number of Pages Required
5+ page
Font styles to use
Sans Serif
Requirements
Must have
- clean design , easy to understand and navigate , our target is the upmarket costumer how are dog lover
Should not have
- NOOO of the shelf design , confusing design , brown colors

```html
<!DOCTYPE html>
<html lang="en">
<head>
<meta charset="utf-8">
<title>Tallowfield Animal Haven</title>
<link href="https://fonts.googleapis.com/css2?family=Roboto:wght@300;400;500;700&family=Roboto+Condensed:wght@300;400;700&display=swap" rel="stylesheet">
<style>
:root{
  --green:#9dc31f;
  --green-dark:#8bb016;
  --pink:#e5375f;
  --ink:#2f2f2f;
  --text:#555;
  --white:#fff;
  --panel:#e6ebee;
  --footer:#1f1f1f;
}
*{box-sizing:border-box;margin:0;padding:0}
html,body{width:1200px;height:2744px;overflow:hidden}
body{position:relative;background:var(--white);font-family:"Roboto",Arial,sans-serif;color:var(--text)}
.abs{position:absolute}

/* hero */
.hero{left:0;top:0;width:1200px;height:686px;background:linear-gradient(115deg,#4a4744 0%,#3b3a3b 35%,#55575a 70%,#6a6d70 100%)}
.hero-photo{left:0;top:0;width:1200px;height:686px;background:radial-gradient(ellipse 360px 300px at 420px 270px,rgba(120,90,60,.55),rgba(0,0,0,0) 70%),radial-gradient(ellipse 300px 220px at 620px 560px,rgba(110,95,80,.45),rgba(0,0,0,0) 70%)}
.hero-band{left:0;top:686px;width:1200px;height:9px;background:var(--green)}
.phone{left:100px;top:60px;display:flex;align-items:center;gap:12px;color:#ddd;font-size:13px}
.phone .num{color:var(--green);font-size:21px;font-weight:500}
.phone-icon{width:36px;height:36px;border:2px solid var(--green);border-radius:50%;display:flex;align-items:center;justify-content:center}
.brand{left:450px;top:52px;width:300px;text-align:center;font-family:"Roboto Condensed",sans-serif;font-weight:700;font-size:34px;color:var(--white);display:flex;align-items:center;justify-content:center;gap:10px}
.brand .dot{width:14px;height:14px;border-radius:50%;background:var(--green)}
.social{display:flex;gap:5px}
.social span{width:45px;height:45px;border:1.5px solid rgba(255,255,255,.85);display:block}
.top-social{left:905px;top:57px}
.nav{left:100px;top:152px;width:1000px;height:51px;border-top:1.5px dotted rgba(255,255,255,.55);border-bottom:1.5px dotted rgba(255,255,255,.55);display:flex;justify-content:space-between;align-items:center;padding:0 8px}
.nav a{color:var(--white);text-decoration:none;font-size:13px;font-weight:500;letter-spacing:.3px}
.nav a.active{color:var(--green)}
.hero-title{right:101px;top:315px;text-align:right;color:var(--white)}
.hero-title h1{font-family:"Roboto Condensed",sans-serif;font-weight:400;font-size:36px;letter-spacing:.3px;white-space:nowrap}
.hero-title p{font-size:13px;line-height:20px;margin-top:12px;color:#eee}
.chev{top:293px}

/* welcome */
.dog-img{left:55px;top:750px;width:603px;height:311px;background:radial-gradient(ellipse 240px 110px at 300px 170px,#e6dfd8,#f5f2ef 70%,#fff 100%)}
.welcome{left:673px;top:569px;width:426px;height:494px;background:var(--panel);padding:38px 32px}
.welcome h2{font-weight:300;font-size:45px;color:var(--pink);line-height:1}
.welcome h3{font-weight:700;font-size:22px;color:var(--pink);margin-top:12px;white-space:nowrap}
.welcome .lead{font-size:12.5px;font-weight:700;color:#444;line-height:20px;margin-top:20px}
.welcome .body{font-size:12.5px;line-height:20.5px;color:#666;margin-top:20px}
.btn-green{display:inline-block;background:var(--green);color:var(--white);font-size:12px;font-weight:700;width:121px;height:41px;line-height:41px;text-align:center;border-radius:3px;margin-top:34px}

/* services */
.services{left:0;top:1123px;width:1200px;height:457px;background:linear-gradient(100deg,#3f4042,#5c5a58 45%,#3c3d3f)}
.services h2{position:absolute;top:45px;width:1200px;text-align:center;font-weight:300;font-size:34px;color:var(--white)}
.service{position:absolute;top:125px;width:280px;text-align:center;color:var(--white)}
.service .icon{width:130px;height:120px;margin:0 auto;border-radius:10px}
.service h4{font-size:19px;font-weight:500;margin-top:38px}
.service p{font-size:12.5px;line-height:19px;color:#ddd;margin-top:10px;padding:0 8px}
.service .more{display:inline-block;margin-top:20px;width:84px;height:30px;line-height:28px;border:1.5px solid #ddd;border-radius:6px;font-size:11px;font-style:italic}
.service.pink .more{border-color:var(--pink);color:var(--pink)}

/* about */
.about{left:100px;top:1628px;width:476px}
.about h2{font-family:"Roboto Condensed",sans-serif;font-weight:300;font-size:37px;color:#333}
.about p{font-size:12.5px;line-height:20.5px;color:#666;margin-top:14px}
.about p+p{margin-top:20px}
.btns{left:99px;top:1890px;display:flex;gap:13px}
.btns span{height:42px;width:152px;border-radius:4px;color:var(--white);font-size:12px;font-weight:700;display:flex;align-items:center;justify-content:space-between;padding:0 14px;white-space:nowrap}
.btns .pink{background:var(--pink)}
.btns .dark{background:#2f2f2f}
.btns .wide{justify-content:center;padding:0 6px;font-size:11.5px}
.video{left:600px;top:1633px;width:499px;height:298px;border:2px solid #ccc;background:linear-gradient(160deg,#5b4a3b,#3f342b 55%,#6a5c4d)}

/* hours band */
.hours{left:0;top:1994px;width:1200px;height:344px;background:var(--green)}
.tour{left:155px;top:2023px;width:892px;height:66px;border:2px solid rgba(255,255,255,.9);border-radius:4px;color:var(--white);font-size:22px;font-weight:500;text-align:center;line-height:62px;white-space:nowrap;overflow:hidden}
.info{left:99px;top:2106px;color:var(--white);width:470px}
.info .open{font-size:19px;color:#2c3a05;white-space:nowrap}
.info .times{font-size:20px;font-weight:700;line-height:29px;margin-top:4px}
.info .addr{font-size:12.5px;line-height:21px;margin-top:10px;color:#f3f7e4}
.book{left:99px;top:2251px;width:281px;height:52px;background:var(--pink);color:var(--white);font-size:18px;font-weight:500;border-radius:4px;text-align:center;line-height:52px}
.photo{top:2138px;width:251px;height:163px;border:3px solid rgba(255,255,255,.7);border-radius:3px}
.photo.one{left:580px;background:linear-gradient(135deg,#8a5a3b,#4f6e8c 60%,#7a6648)}
.photo.two{left:849px;background:linear-gradient(135deg,#c9a96b,#8a7f6e 55%,#d8d0c2)}

/* testimonial */
.quote{left:274px;top:2396px;width:630px;text-align:center;font-size:12px;line-height:22px;color:#555}
.bubble{width:36px;height:30px}
.who{left:350px;top:2484px;width:500px;display:flex;align-items:center;justify-content:center;gap:14px;font-size:17px;color:#333;font-weight:500;white-space:nowrap}
.who i{display:block;width:125px;height:1.5px;background:var(--pink)}
.circ{top:2425px}

/* footer */
.footer{left:0;top:2564px;width:1200px;height:180px;background:var(--footer)}
.flinks{left:99px;top:2608px;width:360px;color:var(--white);font-size:13.5px;line-height:26px;font-weight:500}
.email{left:527px;top:2614px;width:302px;height:42px;display:flex}
.email .field{flex:1;background:var(--white);color:#aaa;font-size:11px;padding-left:12px;line-height:42px}
.email .go{width:68px;background:var(--green);color:var(--white);font-weight:700;font-size:16px;text-align:center;line-height:42px}
.foot-social{left:905px;top:2612px}
.copy{left:0;top:2700px;width:1200px;text-align:center;font-size:12px;color:#8a8a8a}
</style>
</head>
<body>

<section class="abs hero" aria-label="Hero">
  <div class="abs hero-photo" role="img" aria-label="Photo of a happy dog playing with a cat"></div>
</section>
<div class="abs hero-band"></div>

<div class="abs phone">
  <span class="phone-icon"><svg width="16" height="16" viewBox="0 0 24 24"><path d="M6.6 10.8a15.2 15.2 0 0 0 6.6 6.6l2.2-2.2a1 1 0 0 1 1-.25 11.4 11.4 0 0 0 3.6.57 1 1 0 0 1 1 1V20a1 1 0 0 1-1 1A17 17 0 0 1 3 4a1 1 0 0 1 1-1h3.5a1 1 0 0 1 1 1c0 1.25.2 2.45.57 3.57a1 1 0 0 1-.25 1z" fill="#9dc31f"/></svg></span>
  <span>Call Us On :</span><span class="num">(02) 5550 7321</span>
</div>
<div class="abs brand"><span class="dot"></span>Tallowfield</div>
<div class="abs social top-social" aria-label="Social links"><span></span><span></span><span></span><span></span></div>

<nav class="abs nav">
  <a class="active" href="#">HOME</a><a href="#">BOARDING</a><a href="#">DAYCARE</a><a href="#">GROOMING</a><a href="#">TRAINING</a><a href="#">BOUTIQUE</a><a href="#">BLOG</a><a href="#">CONTACT</a><a href="#">ABOUT US</a>
</nav>

<svg class="abs chev" style="left:51px" width="32" height="120" viewBox="0 0 32 120"><polyline points="30,2 2,60 30,118" fill="none" stroke="rgba(255,255,255,.6)" stroke-width="2"/></svg>
<svg class="abs chev" style="left:1118px" width="32" height="120" viewBox="0 0 32 120"><polyline points="2,2 30,60 2,118" fill="none" stroke="rgba(255,255,255,.6)" stroke-width="2"/></svg>

<div class="abs hero-title">
  <h1>LOVE TO PLAY AND MEET MY BUDDIES</h1>
  <p>There are many variations of passages of Lorem Ipsum available, but the<br>majority have suffered alteration in some form</p>
</div>

<div class="abs dog-img" role="img" aria-label="Photo of a bulldog lying on its back"></div>

<section class="abs welcome">
  <h2>WELCOME !</h2>
  <h3>TALLOWFIELD ANIMAL HAVEN!</h3>
  <p class="lead">A pet paradise providing the best pet care in the greater Fort Lauderdale FL area. Professional cat &amp; dog boarding, doggy daycare, pet grooming, training, holistic foods &amp; pet boutique.</p>
  <p class="body">Discover how much Tallowfield has to offer for your pet boarding needs by viewing a virtual tour of our 16,000 s/f 'Home Away From Home'. See 9,000 s/f of air conditioned space and a 4,000 s/f outdoor playground with a splash pool. Why not just come by and take a tour of our Fort Lauderdale FL retail store, grooming salon and air conditioned suites? If you prefer to set a time that is best for you, call us on (954) 555.0148. We're always happy to accommodate you.</p>
  <span class="btn-green">READ MORE</span>
</section>

<section class="abs services" aria-label="Our services">
  <div class="abs" style="inset:0;background:radial-gradient(ellipse 300px 200px at 560px 250px,rgba(140,110,90,.35),rgba(0,0,0,0) 70%)" role="img" aria-label="Photo of a woman hugging her dog"></div>
  <h2>OUR SERVICES</h2>
  <div class="service" style="left:89px">
    <div class="icon" style="background:rgba(255,255,255,.85)" role="img" aria-label="Illustration of a trainer with a dog"></div>
    <h4>DOG TRAINING</h4>
    <p>There are many variations of passages of Lorem Ipsum available, but the majority have suffered alteration in some form</p>
    <span class="more">READ MORE</span>
  </div>
  <div class="service pink" style="left:458px">
    <div class="icon" style="background:var(--pink)" role="img" aria-label="Illustration of a dog and a cat"></div>
    <h4>DOG DAY CAR</h4>
    <p>There are many variations of passages of Lorem Ipsum available, but the majority have suffered alteration in some form</p>
    <span class="more">READ MORE</span>
  </div>
  <div class="service" style="left:831px">
    <div class="icon" style="background:rgba(255,255,255,.85)" role="img" aria-label="Illustration of grooming scissors and a dog"></div>
    <h4>DOG GROOMING</h4>
    <p>There are many variations of passages of Lorem Ipsum available, but the majority have suffered alteration in some form</p>
    <span class="more">READ MORE</span>
  </div>
  <svg class="abs" style="left:51px;top:185px" width="32" height="120" viewBox="0 0 32 120"><polyline points="30,2 2,60 30,118" fill="none" stroke="rgba(255,255,255,.6)" stroke-width="2"/></svg>
  <svg class="abs" style="left:1118px;top:185px" width="32" height="120" viewBox="0 0 32 120"><polyline points="2,2 30,60 2,118" fill="none" stroke="rgba(255,255,255,.6)" stroke-width="2"/></svg>
</section>

<section class="abs about">
  <h2>ABOUT US</h2>
  <p>Discover how much Tallowfield has to offer for your pet boarding needs by viewing a virtual tour of our 16,000 s/f 'Home Away From Home'. See 9,000 s/f of air conditioned space and a 4,000 s/f outdoor playground with a splash pool.</p>
  <p>Let us pamper your pets with our large air conditioned dog boarding suites, raised platform beds, playtime activities, frolicking in the pool, special meal preparations plus the finest in pet grooming and spa services. Our staff will lovingly the care for your special pet from the minute they step into our center until you're ready to the pick them up. We think pets are people, too! For immediate pet boarding</p>
</section>
<div class="abs btns">
  <span class="pink">RESERVATIONS <svg width="12" height="12" viewBox="0 0 12 12"><circle cx="6" cy="6" r="5" fill="none" stroke="#fff" stroke-width="1.3"/><polyline points="5,3.5 7.5,6 5,8.5" fill="none" stroke="#fff" stroke-width="1.3"/></svg></span>
  <span class="dark">OUR RATES <svg width="12" height="12" viewBox="0 0 12 12"><circle cx="6" cy="6" r="5" fill="none" stroke="#fff" stroke-width="1.3"/><polyline points="5,3.5 7.5,6 5,8.5" fill="none" stroke="#fff" stroke-width="1.3"/></svg></span>
  <span class="pink wide">BOUTIQUE &amp; HOLISTIC</span>
</div>
<div class="abs video" role="img" aria-label="Video still of dogs playing inside the daycare room">
  <svg class="abs" style="left:210px;top:110px" width="76" height="76" viewBox="0 0 76 76"><circle cx="38" cy="38" r="38" fill="rgba(255,255,255,.55)"/><polygon points="30,22 56,38 30,54" fill="#fff"/></svg>
</div>

<section class="abs hours"></section>
<div class="abs tour">Click on the image above to take a virtual tour of Tallowfield 16,000 s/f store.</div>
<div class="abs info">
  <p class="open">Our Fort Lauderdale FL facility is open 7 days per week</p>
  <p class="times">Monday – Saturday 7:00 am to 7:00 pm<br>Sunday 9:00 am to 5:00 pm</p>
  <p class="addr">Located at 248 Harbor Crest Causeway just minutes from Port Everglades, airport, A1A, I-95, turnpike &amp; downtown Fort Lauderdale FL.</p>
</div>
<div class="abs book">Book an Appointment Today!</div>
<div class="abs photo one" role="img" aria-label="Photo of a groomer with dogs at the splash pool"></div>
<div class="abs photo two" role="img" aria-label="Photo of a staff member holding two dogs"></div>

<svg class="abs circ" style="left:61px" width="36" height="36" viewBox="0 0 36 36"><circle cx="18" cy="18" r="16" fill="none" stroke="#c8c8c8" stroke-width="2"/><polyline points="21,11 13,18 21,25" fill="none" stroke="#c8c8c8" stroke-width="2"/><line x1="13" y1="18" x2="26" y2="18" stroke="#c8c8c8" stroke-width="2"/></svg>
<svg class="abs circ" style="left:1101px" width="36" height="36" viewBox="0 0 36 36"><circle cx="18" cy="18" r="16" fill="none" stroke="#c8c8c8" stroke-width="2"/><polyline points="15,11 23,18 15,25" fill="none" stroke="#c8c8c8" stroke-width="2"/><line x1="10" y1="18" x2="23" y2="18" stroke="#c8c8c8" stroke-width="2"/></svg>
<svg class="abs bubble" style="left:226px;top:2390px" viewBox="0 0 36 30"><path d="M4 2h28a3 3 0 0 1 3 3v14a3 3 0 0 1-3 3H16l-8 7v-7H4a3 3 0 0 1-3-3V5a3 3 0 0 1 3-3z" fill="#9dc31f"/></svg>
<p class="abs quote">There are many variations of passages of Lorem Ipsum available, but the majority have suffered alteration in some form, by injected humour, or randomised words which don't look even slightly believable. If you are going to use a passage of<br>Ipsum, you need to be sure there isn't anything embarrassing hidden in the middle of text.</p>
<svg class="abs bubble" style="left:856px;top:2452px" viewBox="0 0 36 30"><path d="M32 2H4a3 3 0 0 0-3 3v14a3 3 0 0 0 3 3h16l8 7v-7h4a3 3 0 0 0 3-3V5a3 3 0 0 0-3-3z" fill="#9dc31f"/></svg>
<div class="abs who"><i></i>DANA MORROW<i></i></div>

<footer class="abs footer"></footer>
<div class="abs flinks">Home &nbsp;/&nbsp; Boarding &nbsp;/&nbsp; Daycare &nbsp;/&nbsp; Grooming &nbsp;/&nbsp; Training &nbsp;/<br>Boutique &nbsp;/&nbsp; Blog &nbsp;/&nbsp; Contact &nbsp;/&nbsp; About Us</div>
<div class="abs email"><span class="field">Enter your email</span><span class="go">GO!</span></div>
<div class="abs social foot-social" aria-label="Social links"><span></span><span></span><span></span><span></span></div>
<p class="abs copy">© Copyright 2015-tallowfieldanimalhaven.example - All Rights Reserve | Linden Web Studio | Subscribe to Newsletter</p>

</body>
</html>
```